Company or website name

LumenVault.com.au

Links to the website

n/a

Describe your company and organization and target audience

Lumen Vault makes it easy for Australians to set up automated monthly investments into blue-chip cryptocurrencies. The app is launching soon, and customers can join the waitlist to be first in line when the product launches. Launch is planned for mid-2022. Our target audience are everyday people who want to invest in cryptocurrencies, probably for the first time. They want a simple, trustworthy product that makes it easy to buy crypto.

The design should have the following

Clean and simple and professional. Not cartoonish or gimmicky. The app seeks to target everyday people who are just entering the crypto market. Think more "Banking", "Investing", or "Accounting" and less "Bitcoin" or "Crypto". The landing page should have a form to let users join the waitlist. It could also have the steps to use the product, something like: 1. Create an account. 2. Choose a monthly deposit amount. 3. Deposits are automatically invested. Withdraw anytime! Some example websites we like are https://pivora.app , and https://www.trynelvox.io .

Briefly describe your contest

A website to let people know about a simple investing product coming soon

```html
<!DOCTYPE html>
<html lang="en">
<head>
<meta charset="utf-8">
<title>Lumen Vault — Automated crypto investing</title>
<link href="https://fonts.googleapis.com/css2?family=Poppins:wght@400;500;600;700&display=swap" rel="stylesheet">
<style>
  :root{
    --blue:#1d9fe6;
    --blue-dark:#0f6fc4;
    --navy:#0d2a6b;
    --navy-deep:#0a1d57;
    --ink:#33415c;
    --muted:#7a869c;
    --mint:#eef8f3;
    --hero-bg:#f7f9fc;
    --white:#ffffff;
    --line:#dfe6ef;
  }
  *{box-sizing:border-box;margin:0;padding:0}
  html,body{width:1200px;height:2176px;overflow:hidden}
  body{font-family:"Poppins",sans-serif;color:var(--ink);background:var(--white);position:relative}

  .announce{height:13px;background:var(--blue);color:var(--white);font-size:8px;text-align:center;line-height:13px}

  .nav{height:50px;display:flex;align-items:center;justify-content:space-between;padding:0 70px;background:var(--white);border-bottom:1px solid var(--line)}
  .nav-links{display:flex;gap:26px;font-size:11px;color:var(--navy)}
  .brand{display:flex;align-items:center;gap:8px;font-weight:600;font-size:13px;color:var(--navy)}
  .brand-mark{width:18px;height:18px;background:var(--blue);border-radius:4px}
  .nav-actions{display:flex;align-items:center;gap:22px;font-size:11px;color:var(--navy)}
  .btn{display:inline-block;background:var(--blue);color:var(--white);font-size:11px;font-weight:500;padding:6px 20px;border-radius:4px}

  .hero{height:570px;background:var(--hero-bg);position:relative}
  .hero-copy{position:absolute;left:190px;top:190px;width:470px}
  .hero-title{font-size:31px;line-height:1.3;font-weight:500;color:var(--navy)}
  .hero-sub{margin-top:10px;font-size:12px;color:var(--muted)}
  .hero-sub b{color:var(--blue);font-weight:600}
  .hero-cta{margin-top:22px;display:flex;align-items:center;gap:26px}
  .text-link{font-size:10px;color:var(--blue)}
  .hero-photo{position:absolute;left:672px;top:90px;width:528px;height:312px;border-radius:22px 0 0 22px;background:linear-gradient(135deg,#7c8f6b 0%,#c9b27a 45%,#e9dcc0 70%,#b8b6ae 100%)}
  .launch{position:absolute;left:190px;top:470px}
  .launch-label{font-size:12px;color:var(--navy)}
  .store-badges{margin-top:10px;display:flex;gap:12px}
  .store-badge{width:82px;height:24px;border:1px solid var(--line);border-radius:5px;background:var(--white)}

  .features{height:330px;background:var(--mint);text-align:center;padding-top:82px}
  .section-title{font-size:22px;font-weight:600;color:var(--navy)}
  .feature-row{margin-top:60px;display:flex;justify-content:center;gap:90px}
  .feature{width:200px}
  .feature-icon{width:36px;height:36px;margin:0 auto 10px;border:1.5px solid var(--blue);border-radius:8px;display:flex;align-items:center;justify-content:center}
  .feature-name{font-size:11px;font-weight:600;color:var(--navy)}
  .feature-text{margin-top:4px;font-size:8.5px;line-height:1.5;color:var(--muted)}

  .how{height:680px;position:relative;background:var(--white)}
  .how-photo{position:absolute;left:0;top:80px;width:450px;height:478px;border-radius:0 22px 22px 0;background:linear-gradient(160deg,#d8cbb4 0%,#8a7b66 40%,#3f3b36 75%,#6d5a3f 100%)}
  .how-title{position:absolute;left:600px;top:150px;width:400px;text-align:center;font-size:24px;font-weight:600;color:var(--navy)}
  .steps{position:absolute;left:515px;top:248px;list-style:none}
  .step{display:flex;gap:26px;align-items:flex-start;height:110px}
  .step-num{width:30px;font-size:44px;line-height:1;font-weight:400;color:var(--navy)}
  .step-name{font-size:17px;font-weight:600;color:var(--navy);line-height:1.3;width:440px}
  .step-text{margin-top:6px;font-size:8.5px;color:var(--muted);width:330px;line-height:1.5}

  .notify{height:214px;background:linear-gradient(90deg,#1e8fe0 0%,#2fb4f0 100%);text-align:center;padding-top:44px}
  .notify-title{font-size:19px;font-weight:500;color:var(--white)}
  .notify-form{margin:28px auto 0;width:800px;height:34px;background:var(--white);border-radius:5px;display:flex;align-items:center;justify-content:space-between;padding:0 4px 0 14px}
  .notify-field{display:flex;align-items:center;gap:10px;font-size:10px;color:var(--muted)}
  .notify-form .btn{background:var(--blue-dark);padding:6px 18px;font-size:10px}

  .footer{height:319px;background:var(--navy-deep);color:#b9c4e0;position:relative}
  .footer-brand{position:absolute;left:300px;top:40px;width:240px}
  .footer-logo{width:118px;height:96px;background:var(--white);border-radius:6px;display:flex;align-items:center;justify-content:center;gap:6px;font-size:11px;font-weight:600;color:var(--navy)}
  .footer-logo .brand-mark{width:14px;height:14px}
  .footer-about{margin-top:14px;font-size:8.5px;line-height:1.6}
  .socials{margin-top:14px;display:flex;gap:14px}
  .social{width:14px;height:14px;border-radius:3px;background:#b9c4e0}
  .footer-col{position:absolute;top:48px;font-size:9px;line-height:2}
  .footer-col h4{font-size:10px;font-weight:600;color:var(--white);margin-bottom:4px}
  .footer-col ul{list-style:none}
  .col-about{left:585px}
  .col-resources{left:752px}
  .footer-base{position:absolute;left:300px;right:300px;bottom:22px;border-top:1px solid #25397a;padding-top:12px;display:flex;justify-content:space-between;font-size:8px}
  .footer-legal{display:flex;gap:20px}
</style>
</head>
<body>
  <div class="announce">Launch your crypto journey with Lumen Vault — join the waitlist for early access today</div>

  <header class="nav">
    <nav class="nav-links"><span>How it Works</span><span>Benefits</span><span>Fees</span><span>Company ▾</span></nav>
    <div class="brand"><span class="brand-mark"></span>Lumen Vault</div>
    <div class="nav-actions"><span>Contact us</span><span class="btn">Get Notified</span></div>
  </header>

  <section class="hero">
    <div class="hero-copy">
      <h1 class="hero-title">Adding blue-chip cryptocurrency to your portfolio had never been this easy</h1>
      <p class="hero-sub">Investing regularly in crypto as simple as <b>1-2-3</b></p>
      <div class="hero-cta"><span class="btn">Get Notified</span><span class="text-link">Learn how it works →</span></div>
    </div>
    <div class="hero-photo" role="img" aria-label="Photo of stacked gold coins and a crypto coin beside a small plant"></div>
    <div class="launch">
      <p class="launch-label">Coming in Mid 2022</p>
      <div class="store-badges"><span class="store-badge"></span><span class="store-badge"></span></div>
    </div>
  </section>

  <section class="features">
    <h2 class="section-title">Cryptocurrency investments at your fingertips</h2>
    <div class="feature-row">
      <div class="feature">
        <div class="feature-icon"><svg width="18" height="18" viewBox="0 0 18 18" fill="none" stroke="#e2574c" stroke-width="1.5"><rect x="3" y="2" width="12" height="14" rx="2"/><path d="M6 7h6M6 10h6M6 13h3"/></svg></div>
        <p class="feature-name">Simple Investments</p>
        <p class="feature-text">Set automatic monthly deposits and let your portfolio grow over time.</p>
      </div>
      <div class="feature">
        <div class="feature-icon"><svg width="18" height="18" viewBox="0 0 18 18" fill="none" stroke="#e2574c" stroke-width="1.5"><path d="M9 2l6 2.5v4.5c0 3.5-2.6 6-6 7-3.4-1-6-3.5-6-7V4.5z"/><path d="M6.5 9l2 2 3-3.5"/></svg></div>
        <p class="feature-name">Industry grade security</p>
        <p class="feature-text">Your assets are protected with bank-level encryption and secure custody.</p>
      </div>
      <div class="feature">
        <div class="feature-icon"><svg width="18" height="18" viewBox="0 0 18 18" fill="none" stroke="#e2574c" stroke-width="1.5"><path d="M3 15V9M7.5 15V5M12 15v-7M15.5 15V3"/></svg></div>
        <p class="feature-name">Portfolio Management</p>
        <p class="feature-text">Track your holdings and performance in one clear, simple dashboard.</p>
      </div>
    </div>
  </section>

  <section class="how">
    <div class="how-photo" role="img" aria-label="Photo of a hand pouring gold coins into a glass jar on a wooden table"></div>
    <h2 class="how-title">How It Works</h2>
    <ol class="steps">
      <li class="step"><span class="step-num">1</span><div><p class="step-name">Create an account</p><p class="step-text">Sign up in minutes with your email and verify your identity.</p></div></li>
      <li class="step"><span class="step-num">2</span><div><p class="step-name">Choose a monthly deposit amount</p><p class="step-text">Pick any amount that suits your budget and change it whenever you like.</p></div></li>
      <li class="step"><span class="step-num">3</span><div><p class="step-name">Deposits are automatically invested.<br>Withdraw anytime.</p><p class="step-text">Your deposits buy blue-chip crypto automatically, and you can withdraw funds at any time.</p></div></li>
    </ol>
  </section>

  <section class="notify">
    <h2 class="notify-title">Get notified when we are ready</h2>
    <div class="notify-form">
      <span class="notify-field"><svg width="14" height="10" viewBox="0 0 14 10" fill="none" stroke="#7a869c" stroke-width="1.2"><rect x="0.6" y="0.6" width="12.8" height="8.8" rx="1"/><path d="M1 1l6 4.5L13 1"/></svg>Enter your email address</span>
      <span class="btn">Get Notified</span>
    </div>
  </section>

  <footer class="footer">
    <div class="footer-brand">
      <div class="footer-logo"><span class="brand-mark"></span>Lumen Vault</div>
      <p class="footer-about">Lumen Vault is an Australian platform making regular cryptocurrency investing simple, secure and accessible for everyday people.</p>
      <div class="socials"><span class="social"></span><span class="social"></span><span class="social"></span></div>
    </div>
    <div class="footer-col col-about">
      <h4>About Lumen Vault</h4>
      <ul><li>How it Works</li><li>Benefits</li><li>Security</li><li>About Us</li><li>Blog</li><li>Contact</li></ul>
    </div>
    <div class="footer-col col-resources">
      <h4>Resources</h4>
      <ul><li>Help Centre</li><li>Blog</li><li>Community</li><li>Support</li></ul>
    </div>
    <div class="footer-base">
      <span>© 2022 Lumen Vault. All rights reserved.</span>
      <span class="footer-legal"><span>Privacy Policy</span><span>Terms &amp; Conditions</span></span>
    </div>
  </footer>
</body>
</html>
```